Carpet cleaning company wants business card

Need an exciting new fresh design for business cards for my carpet cleaning /pest control business
www.brightwovecare.com.au
Can design include a lined section for quoting or information? Thanks !

```html
<!DOCTYPE html>
<html lang="en">
<head>
<meta charset="utf-8">
<title>BrightWove Care – Business Card</title>
<link rel="stylesheet" href="https://fonts.googleapis.com/css2?family=Montserrat:wght@400;500;700&display=swap">
<style>
  :root {
    --brand-blue: #0b55a0;
    --brand-red: #e8403a;
    --ink: #1d1d1f;
    --card-white: #ffffff;
    --backdrop: #e9e7e3;
  }
  html, body {
    margin: 0;
    padding: 0;
    width: 900px;
    height: 1200px;
    overflow: hidden;
    background: var(--backdrop);
    font-family: "Montserrat", Arial, sans-serif;
  }
  .canvas {
    position: relative;
    width: 900px;
    height: 1200px;
  }
  .card {
    position: absolute;
    width: 742px;
    height: 440px;
    border-radius: 24px;
    overflow: hidden;
    box-shadow: 0 6px 16px rgba(0,0,0,0.25);
  }
  .card-front {
    left: 80px;
    top: 131px;
    background: var(--card-white);
  }
  .card-back {
    left: 79px;
    top: 638px;
    background: var(--brand-blue);
    display: flex;
    align-items: center;
    justify-content: center;
  }
  .wave {
    position: absolute;
    left: 0;
    bottom: 0;
    width: 742px;
    height: 440px;
  }
  .front-brand {
    position: absolute;
    left: 112px;
    top: 186px;
    margin: 0;
    font-weight: 700;
    font-size: 22px;
    color: var(--brand-blue);
    letter-spacing: -0.2px;
  }
  .contact {
    position: absolute;
    left: 357px;
    top: 114px;
    height: 195px;
    padding-left: 16px;
    border-left: 2px solid var(--brand-red);
    color: var(--ink);
  }
  .contact-name {
    margin: 0;
    font-size: 25px;
    font-weight: 700;
    color: var(--brand-red);
    line-height: 1;
    padding-top: 1px;
  }
  .contact-role {
    margin: 7px 0 0;
    font-size: 16px;
    font-weight: 400;
  }
  .contact-address {
    margin: 13px 0 0;
    font-style: normal;
    font-size: 16px;
    line-height: 20px;
  }
  .contact-list {
    list-style: none;
    margin: 12px 0 0;
    padding: 0;
    font-size: 16px;
  }
  .contact-list li {
    display: flex;
    align-items: center;
    height: 31px;
  }
  .contact-list svg {
    width: 14px;
    height: 14px;
    margin: 0 11px 0 2px;
    fill: var(--brand-red);
    flex: none;
  }
  .back-brand {
    margin: 0;
    font-weight: 700;
    font-size: 62px;
    color: #ffffff;
    letter-spacing: -1px;
  }
</style>
</head>
<body>
<main class="canvas">
  <section class="card card-front" aria-label="Card front">
    <svg class="wave" viewBox="0 0 742 440" aria-hidden="true">
      <path d="M0,358 C130,328 260,338 380,372 C520,410 650,398 742,362 L742,440 L0,440 Z" fill="var(--brand-blue)"/>
      <path d="M168,343 C330,350 470,402 600,392 C660,386 705,362 742,330 L742,358 C690,390 620,410 540,410 C460,408 400,385 340,368 C280,352 220,346 168,343 Z" fill="var(--brand-red)"/>
    </svg>

    <p class="front-brand">BrightWove Care</p>

    <div class="contact">
      <h1 class="contact-name">Aaron Leclair</h1>
      <p class="contact-role">Managing Director</p>
      <address class="contact-address">27 Kestrel Bend Road<br>Oakdale, MS 39245</address>
      <ul class="contact-list">
        <li>
          <svg viewBox="0 0 24 24"><path d="M6.6 10.8a15 15 0 0 0 6.6 6.6l2.2-2.2a1 1 0 0 1 1-.25 11.4 11.4 0 0 0 3.6.57 1 1 0 0 1 1 1V20a1 1 0 0 1-1 1A17 17 0 0 1 3 4a1 1 0 0 1 1-1h3.5a1 1 0 0 1 1 1c0 1.25.2 2.45.57 3.57a1 1 0 0 1-.25 1z"/></svg>
          888.555.0142
        </li>
        <li>
          <svg viewBox="0 0 24 24"><path d="M2 5h20v14H2z M2 5l10 8 10-8" fill="var(--brand-red)"/><path d="M3 6l9 7 9-7" fill="none" stroke="#fff" stroke-width="1.6"/></svg>
          info@brightwovecare.com.au
        </li>
        <li>
          <svg viewBox="0 0 24 24"><circle cx="12" cy="12" r="10"/><path d="M2 12h20M12 2c3 3 3 17 0 20M12 2c-3 3-3 17 0 20" fill="none" stroke="#fff" stroke-width="1.4"/></svg>
          www.brightwovecare.com.au
        </li>
      </ul>
    </div>
  </section>

  <section class="card card-back" aria-label="Card back">
    <p class="back-brand">BrightWove Care</p>
  </section>
</main>
</body>
</html>
```